Non Profit Company Looking For New Website

The website for Corvale Paddock Rehoming Society should offer the viewer beautiful photos that inspire condifence and joy and tap into our love of horses.

We would like to see a website that displays trust, quality and confidence. Needs to be responsive and mobile friendly for all browsers and coded for both Android & IOS.

READ ATTACHED WEBSITE TEMPLATE FOR COMPLETE DETAILS ON WHAT WE ARE LOOKING FOR.

Looking for recommmendations if we should use WordPress/WooCommerce for site or Wordpress with Shopify Plug in or just Shopify.

Must be both desktop and mobile friendly with fast page load speed. Need the ability to edit ourselves.

Industry/Entity Type

Non Profit

Coding

Coded - Design and coding required

Number of Pages Required

5+ page

Requirements
Must have
• We would like to see a website that displays trust, quality and confidence. Needs to be responsive and mobile friendly for all browsers and coded for both Android & IOS.

Looking for recommendations if we should use WordPress/WooCommerce for site or Wordpress with Shopify Plug in or just Shopify.

Logo Colour:
Pantone 7621 C

READ TEMPLATE THAT IS ATTACHED
Nice to have
• Like look of this website as a sample:
https://www.quillmanegallop.com/

Another similar non profit organization
https://brindlefieldrest.com/

```html
<!DOCTYPE html>
<html lang="en">
<head>
<meta charset="utf-8">
<title>Corvale Paddock Rehoming Society</title>
<link href="https://fonts.googleapis.com/css2?family=Playfair+Display:wght@400;700;900&family=Poppins:wght@400;500;600;700&display=swap" rel="stylesheet">
<style>
:root{
  --red:#c3202f;
  --ink:#1b1b1b;
  --text:#444;
  --mist:#ececec;
  --field:#f3f3f3;
  --night:#161616;
  --barn:#3b150b;
}
*{box-sizing:border-box;margin:0;padding:0}
html,body{width:1200px;height:3866px;overflow:hidden}
body{position:relative;background:#fff;font-family:'Poppins',sans-serif;color:var(--text)}
.abs{position:absolute}
.serif{font-family:'Playfair Display',serif}

/* header */
.brand{left:88px;top:20px;width:130px;text-align:center;font-family:'Playfair Display',serif;color:var(--red);font-size:20px;line-height:1.25;font-weight:400}
.nav{right:88px;top:44px;display:flex;gap:30px;font-family:'Playfair Display',serif;font-size:18px;color:var(--ink)}
.nav .on{color:var(--red)}

/* hero */
.hero-bg{left:0;top:0;width:1200px;height:800px}
.hero-photo{left:560px;top:130px;width:640px;height:660px;border-radius:48% 0 40% 46%;background:radial-gradient(ellipse at 50% 45%,#8a4520 0%,#6b3418 35%,#3c6e2a 72%,#2f5a22 100%)}
.hero-title{left:88px;top:295px;font-size:64px;line-height:1;font-weight:700;color:var(--ink)}
.hero-sub{left:88px;top:432px;font-size:23px;line-height:1.3;color:#333}

/* intro */
.intro-title{left:0;width:1200px;top:860px;text-align:center;font-size:50px;font-weight:700;color:var(--ink)}
.intro-text{left:280px;width:640px;top:920px;text-align:center;font-size:18px;line-height:1.6}

.what-photo{left:90px;top:975px;width:458px;height:555px}
.what-title{left:591px;top:1068px;font-size:45px;line-height:1;font-weight:700;color:var(--ink)}
.what-text{left:591px;top:1166px;width:525px;font-size:14px;line-height:22px}
.what-text p{margin-bottom:8px}
.btn-red{display:inline-block;background:var(--red);color:#fff;font-weight:600;font-size:15px;letter-spacing:.5px;padding:10px 20px}
.what-btn{left:591px;top:1322px}

/* adopt band */
.band{left:0;top:1560px;width:1200px;height:508px}
.band-title{left:88px;top:1765px;font-size:45px;font-weight:700;color:#fff}
.band-text{left:88px;top:1826px;width:420px;font-size:16px;line-height:1.4;color:#fff}
.btn-white{left:88px;top:1881px;background:#fff;color:var(--red);font-weight:600;font-size:15px;padding:8px 18px;letter-spacing:.5px}

/* gallery */
.gal-title{left:0;width:1200px;top:2148px;text-align:center;font-size:45px;font-weight:700;color:var(--ink)}
.tabs{left:0;width:1200px;top:2207px;display:flex;justify-content:center;gap:24px;font-size:16px;font-weight:500;color:#333;letter-spacing:.5px}
.tabs .on{color:var(--red)}
.tile{width:335px;height:249px}
.card{left:433px;top:2517px;width:334px;height:249px;background:linear-gradient(160deg,#c7494f,#b8343b);padding:12px}
.card-in{background:var(--red);width:100%;height:100%;padding:50px 16px 0;color:#fff}
.card h3{font-family:'Playfair Display',serif;font-size:21px;font-weight:700;margin-bottom:8px}
.card dl{font-size:10px;line-height:1.75;white-space:nowrap}
.card b{font-weight:700;display:inline-block;width:58px}
.card .row span{margin-right:10px}
.card-btns{margin-top:10px;display:flex;gap:12px;align-items:center;font-size:10px;font-weight:600}
.card-btns .w{background:#fff;color:#222;padding:5px 10px}
.btn-outline{left:486px;top:2799px;width:217px;height:39px;border:2px solid var(--red);color:#222;font-weight:600;font-size:15px;letter-spacing:.8px;text-align:center;line-height:35px}

/* contact */
.q-title{left:0;width:1200px;top:2905px;text-align:center;font-size:45px;line-height:1;font-weight:700;color:var(--ink)}
.q-sub{left:0;width:1200px;top:2994px;text-align:center;font-size:15px}
.info{left:189px;display:flex;gap:24px;align-items:flex-start}
.ico{width:52px;height:52px;border:2px solid var(--red);display:flex;align-items:center;justify-content:center}
.info h4{color:var(--red);font-size:18px;font-weight:700;line-height:1.2}
.info p{font-size:15px;color:#444}
.field{background:var(--field);font-size:12px;color:#555;padding:12px 18px}
.captcha{left:498px;top:3249px;width:174px;height:42px;border:1px solid #ccc;background:#f9f9f9;font-size:9px;display:flex;align-items:center;gap:8px;padding:0 8px}
.captcha i{display:block;width:14px;height:14px;border:2px solid #bbb;background:#fff}
.submit{left:498px;top:3301px;background:var(--red);color:#fff;font-weight:600;font-size:14px;padding:7px 20px;letter-spacing:.5px}

/* footer */
.foot{left:0;top:3360px;width:1200px;height:506px}
.f-brand{left:100px;top:3572px;width:180px;text-align:center;font-family:'Playfair Display',serif;color:var(--red);font-size:26px;line-height:1.35}
.f-col h5{color:#fff;font-size:18px;font-weight:700;margin-bottom:14px;letter-spacing:.3px}
.f-col li{list-style:none;color:#ddd;font-size:13px;line-height:25px}
.f-col p{color:#ddd;font-size:13px}
.mail{margin-top:14px;display:flex;width:240px;height:36px}
.mail span{flex:1;background:#2a2a2a;color:#ccc;font-size:12px;padding:10px 14px}
.mail em{width:38px;background:var(--red);display:flex;align-items:center;justify-content:center}
.dots{display:flex;gap:12px;margin-top:12px}
.dots i{width:11px;height:11px;border-radius:50%;background:#ddd;display:block}
.f-info{display:flex;gap:16px;margin-bottom:14px}
.f-info .ico{width:42px;height:42px}
.f-info h6{color:var(--red);font-size:14px;font-weight:700;line-height:1.2}
.f-info p{color:#ddd;font-size:12px}
.rule{left:88px;top:3810px;width:1024px;height:1px;background:#333}
.copy{left:0;width:1200px;top:3834px;text-align:center;color:#eee;font-size:12px;font-weight:600}
.top{left:1128px;top:3798px;width:30px;height:30px;border-radius:50%;background:var(--red)}
</style>
</head>
<body>

<svg class="abs hero-bg" viewBox="0 0 1200 800" aria-hidden="true">
  <rect width="1200" height="800" fill="#ececec"/>
  <path d="M0 772 C 300 690, 700 640, 1200 640 L1200 800 L0 800 Z" fill="#fff"/>
</svg>
<div class="abs hero-photo" role="img" aria-label="Bay thoroughbred horse walking across a patch of green grass"></div>

<div class="abs brand">CORVALE<br>PADDOCK<br>REHOMING</div>
<nav class="abs nav"><span class="on">Home</span><span>About</span><span>Adopt</span><span>Horses</span><span>Donate/Shop</span><span>Contact</span></nav>

<h1 class="abs hero-title serif">We support and<br>develop retired</h1>
<p class="abs hero-sub">thoroughbred racehorses for their<br>next chapter in life</p>

<h2 class="abs intro-title serif">Retire. Retrain. Rehome.</h2>
<p class="abs intro-text">Corvale Paddock Rehoming Society (CPRS) is a registered not-for-profit organization in Alberta.</p>

<svg class="abs what-photo" viewBox="0 0 458 555" role="img" aria-label="Dark bay horse in a bridle trotting forward out of a triangular paddock scene">
  <defs>
    <radialGradient id="tri" cx=".55" cy=".55" r=".6"><stop offset="0" stop-color="#2a1e17"/><stop offset=".55" stop-color="#4a3a2a"/><stop offset="1" stop-color="#9aa06a"/></radialGradient>
  </defs>
  <polygon points="229,30 458,435 0,435" fill="url(#tri)"/>
</svg>

<h2 class="abs what-title serif">What is Thoroughbred<br>Aftercare?</h2>
<div class="abs what-text">
  <p>The health, safety and welfare of our equine athletes does not end at the finish line, and retirement and aftercare are critical to the success of the racing industry.</p>
  <p>Aftercare is the safe placement of racehorses after their careers as race-horse are completed. Some horses might retire to the breeding shed or broodmare bands, while others are retrained for second careers.</p>
</div>
<a class="abs what-btn btn-red">LEARN MORE ABOUT US</a>

<svg class="abs band" viewBox="0 0 1200 508" role="img" aria-label="Chestnut horse in a halter standing before a dark wooden barn wall">
  <defs>
    <linearGradient id="barn" x1="0" y1="0" x2="1" y2="0"><stop offset="0" stop-color="#2e0f06"/><stop offset=".5" stop-color="#4a1a0c"/><stop offset="1" stop-color="#6e2c14"/></linearGradient>
    <radialGradient id="horse" cx=".72" cy=".55" r=".35"><stop offset="0" stop-color="#9c4a22"/><stop offset="1" stop-color="#9c4a22" stop-opacity="0"/></radialGradient>
  </defs>
  <path d="M0 60 C 150 10, 400 -5, 620 40 L 880 70 C 1000 110, 1120 130, 1200 150 L1200 508 L0 508 Z" fill="url(#barn)"/>
  <path d="M0 60 C 150 10, 400 -5, 620 40 L 880 70 C 1000 110, 1120 130, 1200 150 L1200 508 L0 508 Z" fill="url(#horse)"/>
</svg>
<h2 class="abs band-title serif">Adopt a Horse</h2>
<p class="abs band-text">Corvale Paddock Rehoming Society is committed to helping match you with the perfect horse.</p>
<a class="abs btn-white">ADOPT NOW</a>

<h2 class="abs gal-title serif">Adopt A Horse</h2>
<div class="abs tabs"><span class="on">All</span><span>Thoroughbreds</span><span>Standardbreds</span></div>

<div class="abs tile" style="left:88px;top:2256px;background:linear-gradient(120deg,#1e1712,#4a3a30 60%,#b8a89a)" role="img" aria-label="Dark horse being led by a handler outside a stable"></div>
<div class="abs tile" style="left:433px;top:2256px;background:linear-gradient(180deg,#9aa39a,#6b3a1e 45%,#c9c6c0)" role="img" aria-label="Bay horse standing in a sandy yard"></div>
<div class="abs tile" style="left:777px;top:2256px;background:linear-gradient(180deg,#cfd8d6,#b47a48 50%,#8fa25c)" role="img" aria-label="Chestnut horse trotting through a grassy field"></div>
<div class="abs tile" style="left:88px;top:2517px;background:linear-gradient(180deg,#7ea05a,#d6d6d2 50%,#5e8a3a)" role="img" aria-label="Grey horse cantering across green pasture"></div>
<div class="abs tile" style="left:777px;top:2517px;background:linear-gradient(110deg,#b9a591,#1e1e1e 45%,#b45a2c)" role="img" aria-label="Rider standing beside a chestnut horse"></div>

<div class="abs card" role="group" aria-label="Featured horse">
  <div class="card-in">
    <h3>Bramblewick</h3>
    <dl>
      <div><b>FEE</b> $1,000—NOW $800 UNTIL 5/31</div>
      <div><b>Height</b> 16.1</div>
      <div class="row"><b>Birth Year</b> <span>2007</span> Color &nbsp;Bay</div>
      <div class="row"><b>Gender</b> <span>Gelding</span> Location &nbsp;HOLLIN RIDGE</div>
    </dl>
    <div class="card-btns"><span class="w">VIEW MORE ON THIS HORSE</span><span>VIEW All HORSES</span></div>
  </div>
</div>

<a class="abs btn-outline">MORE WAYS TO GIVE</a>

<h2 class="abs q-title serif">Have a question or need<br>more information</h2>
<p class="abs q-sub">Give us a call or use the form below.</p>

<div class="abs info" style="top:3058px">
  <div class="ico"><svg width="18" height="22" viewBox="0 0 18 22"><path d="M9 0C4 0 0 4 0 9c0 6 9 13 9 13s9-7 9-13C18 4 14 0 9 0z" fill="#c3202f"/><circle cx="9" cy="9" r="3" fill="#fff"/></svg></div>
  <div><h4>LOATION</h4><p>Some goes address here</p></div>
</div>
<div class="abs info" style="top:3121px">
  <div class="ico"><svg width="20" height="14" viewBox="0 0 20 14"><rect width="20" height="14" fill="#c3202f"/><path d="M0 0l10 8 10-8" stroke="#fff" stroke-width="1.5" fill="none"/></svg></div>
  <div><h4>EMAIL</h4><p>hello@corvalepaddock.org</p></div>
</div>
<div class="abs info" style="top:3187px">
  <div class="ico"><svg width="18" height="18" viewBox="0 0 24 24"><path d="M6.6 10.8a15 15 0 006.6 6.6l2.2-2.2c.3-.3.7-.4 1-.2 1.1.4 2.3.6 3.6.6.6 0 1 .4 1 1V20c0 .6-.4 1-1 1A17 17 0 013 4c0-.6.4-1 1-1h3.5c.6 0 1 .4 1 1 0 1.3.2 2.5.6 3.6.1.3 0 .7-.2 1z" fill="#c3202f"/></svg></div>
  <div><h4>CALL NOW</h4><p>403 555 0147</p></div>
</div>

<div class="abs field" style="left:498px;top:3057px;width:246px">First name*</div>
<div class="abs field" style="left:749px;top:3057px;width:246px">Last name*</div>
<div class="abs field" style="left:498px;top:3100px;width:246px">Your phone*</div>
<div class="abs field" style="left:749px;top:3100px;width:246px">Your email*</div>
<div class="abs field" style="left:498px;top:3144px;width:497px;height:96px">How can we hrlp you?</div>
<div class="abs captcha"><i></i><span style="flex:1">I'm not a robot</span><span style="width:14px;height:14px;background:#9bb0d4;display:block"></span></div>
<a class="abs submit">SUBMIT</a>

<svg class="abs foot" viewBox="0 0 1200 506" aria-hidden="true">
  <path d="M0 150 C 300 90, 700 40, 1000 20 C 1100 15, 1160 25, 1200 40 L1200 506 L0 506 Z" fill="#161616"/>
</svg>

<div class="abs f-brand">CORVALE<br>PADDOCK<br>REHOMING</div>

<div class="abs f-col" style="left:396px;top:3563px">
  <h5>Useful Links</h5>
  <ul><li>Home</li><li>About</li><li>Adopt</li><li>Horses</li><li>Donate/Shop</li><li>Contact</li></ul>
</div>
<div class="abs f-col" style="left:600px;top:3563px">
  <h5>Follow Us</h5>
  <p>Subscribe to our newsletter</p>
  <div class="mail"><span>Enter your email</span><em><svg width="14" height="14" viewBox="0 0 14 14"><path d="M0 6l14-6-5 14-2-6z" fill="#fff"/></svg></em></div>
  <div class="dots"><i></i><i></i><i></i><i></i></div>
</div>
<div class="abs f-col" style="left:896px;top:3563px">
  <h5>Contact Us</h5>
  <div class="f-info"><div class="ico"><svg width="12" height="16" viewBox="0 0 18 22"><path d="M9 0C4 0 0 4 0 9c0 6 9 13 9 13s9-7 9-13C18 4 14 0 9 0z" fill="#c3202f"/></svg></div><div><h6>LOATION</h6><p>Some goes address here</p></div></div>
  <div class="f-info"><div class="ico"><svg width="14" height="10" viewBox="0 0 20 14"><rect width="20" height="14" fill="#c3202f"/></svg></div><div><h6>EMAIL</h6><p>hello@corvalepaddock.org</p></div></div>
  <div class="f-info"><div class="ico"><svg width="14" height="14" viewBox="0 0 24 24"><path d="M6.6 10.8a15 15 0 006.6 6.6l2.2-2.2c.3-.3.7-.4 1-.2 1.1.4 2.3.6 3.6.6.6 0 1 .4 1 1V20c0 .6-.4 1-1 1A17 17 0 013 4c0-.6.4-1 1-1h3.5c.6 0 1 .4 1 1 0 1.3.2 2.5.6 3.6.1.3 0 .7-.2 1z" fill="#c3202f"/></svg></div><div><h6>CALL NOW</h6><p>403 555 0147</p></div></div>
</div>

<div class="abs rule"></div>
<p class="abs copy">©Copyright 2021 | All Rights Reserved</p>
<div class="abs top"><svg width="30" height="30" viewBox="0 0 30 30"><path d="M11 17l4-4 4 4" stroke="#fff" stroke-width="2" fill="none"/></svg></div>

</body>
</html>
```